Fresh & Clean *NEW* BUSINESS CARD Needed - OPTOMETRY Clinic/Optical

High-tech optometry practice with 3 doctors seeking new business card.  We provide eye exams, sell, designer glasses/contacts/specialty eyewear and treat ocular diseases.  For our business cards, we are seeking fresh, clean, and crisp design as we grow our team (staffing change).  Simply adding doctors is making the card look busy/cluttered.
 Looking for professional, less cluttered look yet still have our logo, doctor names, phone, address, and website....If possible!  :)
Names:
Marcia Trelford, O.D.
Ned Pallister, O.D.
Oona Ferrant, O.D.
Phone: 555-014-2738
Website: www.BrightLensHub.example
Address:  417 Garnet R. Holloway, Larkfield, QX 00000
Ultimately we have the main business card with all doctor sames and that card has two versions  (front is always the same).  The back has two designs (1) displays next appointment time/date, (2) for "general use" (non-appointment.)    I have attached what we have used in the past.  
We also need a design template for each team member in our practice with their name, title, and email.   Those should be designed with the "general use" back (see attached).
**Open to entirely new design so don't feel obligated to keep current format.  Need new perspective!  Also including our watermark and some other design features we have consistently used in past in our portfolio.  Included are two options for logos--vertical and horizontal.
**I also would like to remove "Member of Sight Alliance" on our logo if possible**
 Other image files available upon request.

Target Market(s)

New patient & Current Patients

Industry/Entity Type

Optometry

Contact Information for Business Card

High-tech optometry practice with 3 doctors seeking new business card.  We provide eye exams, sell, designer glasses/contacts/specialty eyewear and treat ocular diseases.  For our business cards, we are seeking fresh, clean, and crisp design as we grow our team (staffing change).  Simply adding doctors is making the card look busy/cluttered.  Looking for professional, less cluttered look yet still have our logo, doctor names, phone, address, and website....If possible!  :) Names: Marcia Trelford, O.D. Ned Pallister, O.D. Oona Ferrant, O.D. Phone: 555-014-2738 Website: www.BrightLensHub.example Address:  417 Garnet R. Holloway, Larkfield, QX 00000 Ultimately we have the main business card with all doctor sames and that card has two versions  (front is always the same).  The back has two designs (1) displays next appointment time/date, (2) for "general use" (non-appointment.)    I have attached what we have used in the past.   We also need a design template for each team member in our practice with their name, title, and email.   Those should be designed with the "general use" back (see attached). **Open to entirely new design so don't feel obligated to keep current format.  Need new perspective!  Also including our watermark and some other design features we have consistently used in past in our portfolio.  Included are two options for logos--vertical and horizontal. **I also would like to remove "Member of Sight Alliance" on our logo if possible**  Other image files available upon request.

Font styles to use
Other font styles liked:
• We have used Montserrat / Yellowtail in the past

Colors

Designer to choose colors to be used in the design.

Requirements
Must have
• Clean & Fresh Design with Logo / Info provided in description. Horizontal orientation. **I have included the CMYK colors we currently have in our logo.
Should not have
• Cluttered

```html
<!DOCTYPE html>
<html lang="en">
<head>
<meta charset="utf-8">
<title>Bright Lens Hub – Appointment Card</title>
<link href="https://fonts.googleapis.com/css2?family=Nunito:wght@400;700&display=swap" rel="stylesheet">
<style>
  :root {
    --backdrop: #959595;
    --card-white: #ffffff;
    --card-grey: #c2c2c2;
    --ink: #6b6c6e;
    --ink-soft: #7a7b7d;
    --teal: #a4dce0;
    --white: #ffffff;
  }
  * { box-sizing: border-box; margin: 0; padding: 0; }
  html, body { width: 1200px; height: 1000px; overflow: hidden; }
  body {
    background: var(--backdrop);
    font-family: "Nunito", sans-serif;
    color: var(--ink);
    position: relative;
  }
  .card {
    position: absolute;
    left: 315px;
    width: 568px;
    height: 327px;
    border-radius: 24px;
    overflow: hidden;
  }
  .card-front { top: 153px; background: var(--card-white); }
  .card-back { top: 518px; background: var(--card-grey); }

  /* front */
  .brand {
    position: absolute;
    left: 23px; top: 27px;
    display: flex; align-items: center; gap: 12px;
  }
  .brand-dot {
    width: 64px; height: 64px; border-radius: 50%;
    background: var(--teal);
    flex: none;
  }
  .brand-name {
    font-size: 30px; font-weight: 400; line-height: 1;
    color: var(--ink);
  }
  .doctors {
    position: absolute; left: 27px; top: 134px;
    list-style: none;
    font-size: 27px; line-height: 34px; font-weight: 400;
  }
  .appointment {
    position: absolute; left: 331px; top: 88px; width: 210px;
  }
  .field {
    display: flex; align-items: flex-end;
    font-size: 20px; height: 28px; margin-bottom: 6px;
  }
  .field-line {
    flex: 1; height: 20px; margin-left: 3px;
    border-bottom: 1px solid var(--ink);
    font-size: 16px; text-align: center; line-height: 18px;
  }
  .days {
    display: flex; justify-content: space-between;
    margin-top: 18px; width: 205px;
  }
  .day {
    width: 29px; height: 28px;
    border: 1px solid var(--ink);
    box-shadow: 1px 1px 0 var(--ink);
    font-size: 12px; display: flex; align-items: center; justify-content: center;
  }
  .notice {
    margin-top: 14px; width: 205px;
    font-size: 10px; line-height: 12px; text-align: center; color: var(--ink-soft);
  }
  .divider {
    position: absolute; left: 27px; top: 245px;
    width: 514px; height: 2px; background: var(--teal);
  }
  .contact {
    position: absolute; left: 27px; top: 259px;
    font-size: 17px; line-height: 22px;
  }
  .contact .phone { font-weight: 700; }
  .url strong { font-weight: 700; }
  .address {
    position: absolute; right: 27px; top: 259px;
    font-size: 17px; line-height: 22px; text-align: right; font-style: normal;
  }

  /* back */
  .back-brand {
    position: absolute; left: 61px; top: 116px;
    display: flex; align-items: center; gap: 12px;
  }
  .back-brand .brand-dot { width: 78px; height: 78px; }
  .back-brand .brand-name { font-size: 46px; color: var(--white); }
  .contact-pill {
    position: absolute; left: 94px; top: 237px;
    width: 379px; height: 36px; border-radius: 18px;
    background: var(--white);
    display: flex; align-items: center; padding-left: 7px;
    font-size: 14px; color: var(--ink);
  }
  .pill-icon {
    width: 26px; height: 26px; border-radius: 50%;
    background: var(--teal);
    display: flex; align-items: center; justify-content: center;
    margin-right: 7px;
    flex: none;
  }
  .pill-phone { font-weight: 700; margin-right: 8px; }
</style>
</head>
<body>

<section class="card card-front">
  <div class="brand">
    <span class="brand-dot"></span>
    <span class="brand-name">Bright Lens<br>Hub</span>
  </div>

  <ul class="doctors">
    <li>Marcia Trelford, O.D.</li>
    <li>Ned Pallister, O.D.</li>
    <li>Oona Ferrant, O.D.</li>
  </ul>

  <div class="appointment">
    <div class="field">Date:<span class="field-line">/</span></div>
    <div class="field">Time:<span class="field-line">:</span></div>
    <div class="days">
      <span class="day">M</span><span class="day">T</span><span class="day">W</span><span class="day">T</span><span class="day">F</span>
    </div>
    <p class="notice">*If your unable to keep your appointment<br>kindly give us 24 hour notice</p>
  </div>

  <div class="divider"></div>

  <div class="contact">
    <div class="phone">(555) 014-2738</div>
    <div class="url"><strong>BrightLensHub</strong>.example</div>
  </div>
  <address class="address">417 Garnet R. Holloway<br>Larkfield, QX 00000</address>
</section>

<section class="card card-back">
  <div class="back-brand">
    <span class="brand-dot"></span>
    <span class="brand-name">Bright Lens Hub</span>
  </div>

  <div class="contact-pill">
    <span class="pill-icon">
      <svg width="14" height="14" viewBox="0 0 24 24" aria-hidden="true">
        <path fill="#6b6c6e" d="M6.6 10.8a15.1 15.1 0 0 0 6.6 6.6l2.2-2.2a1 1 0 0 1 1-.25 11.4 11.4 0 0 0 3.6.57 1 1 0 0 1 1 1V20a1 1 0 0 1-1 1A17 17 0 0 1 3 4a1 1 0 0 1 1-1h3.5a1 1 0 0 1 1 1c0 1.25.2 2.460.57 3.6a1 1 0 0 1-.25 1z"/>
      </svg>
    </span>
    <span class="pill-phone">(555) 014-2738</span>
    <span class="pill-icon">
      <svg width="16" height="16" viewBox="0 0 24 24" aria-hidden="true" fill="none" stroke="#6b6c6e" stroke-width="1.6">
        <circle cx="12" cy="12" r="9"/>
        <ellipse cx="12" cy="12" rx="4" ry="9"/>
        <path d="M3 12h18M4.5 7.5h15M4.5 16.5h15"/>
      </svg>
    </span>
    <span class="url"><strong>BrightLensHub</strong>.example</span>
  </div>
</section>

</body>
</html>
```